Name of company is Bluebird Meadow Shear Sharpening and Sales.Card design basic idea; I'm thinking back side just showing a sharp BLUEBIRD MEADOW. Front side: I'm thinking a tiger showing teeth and claws.With the words "Bluebird Meadow" larger type emphasized on one line.Then "Shear Sharpening and Sales" on the next line.Other info on front of card should be my name and phone #'s and address: Marcus Pellingham P (407)555-0174 CP (321)555-0138 My address is NOT to be emphasized.Can go at bottom of card. It is: 5127 Brennigan Lane Orlando FL 32899 If all that's too much to fit without looking cluttered than maybe the claw on the front with all the contact info. and just the Tiger on back of card. Whichever looks best.

Target Market(s)

Beauty Salons

Industry/Entity Type

It Company

Contact Information for Business Card

The 2 images,the claw and the tiger,could be either illustrations or photos.Whatever looks best.Got to be eye grabbing either way.

Requirements
Must have
• Contact info. Must be in color. And emphasize the identity. BLUEBIRD MEADOW.Tiger on one side.Showing TEETH. Bluebird Meadow on the other side. Showing the CLAW. .Both pics must emphasize SHARPNESS...This is a shear SHARPENING business. If one of the claw pics shows cutting grooves into something that's fine too. Card must show sharpness of the claw blade somehow.
Nice to have
• Attention grabbing. Images should jump off the card!
Should not have
• No boring cuddly tiger pics showing no teeth or claws or dull teeth or claws. No Black and whites.. No extra words other than what I've listed.

```html
<!DOCTYPE html>
<html lang="en">
<head>
<meta charset="UTF-8">
<title>Bluebird Meadow Shear Sharpening and Sales – Business Card</title>
<link href="https://fonts.googleapis.com/css2?family=Libre+Baskerville:wght@400;700&display=swap" rel="stylesheet">
<style>
  :root {
    --page-bg: #2a2a2b;
    --card-black: #0b0b0b;
    --band-black: #060606;
    --text-white: #ffffff;
    --text-soft: #e4e4e4;
    --fur-orange: #c46f2e;
    --fur-amber: #dc9a55;
    --fur-gold: #e8b577;
    --fur-cream: #ece4da;
    --fur-dark: #2e2016;
    --leaf-green: #7d8a4c;
    --leaf-deep: #2b3520;
    --bark-brown: #4e2f1e;
    --claw-pink: #d9a9a0;
  }
  * { box-sizing: border-box; margin: 0; padding: 0; }
  html, body { width: 1200px; height: 880px; overflow: hidden; }
  body {
    background: var(--page-bg);
    font-family: "Libre Baskerville", "Times New Roman", serif;
    position: relative;
  }
  .card {
    position: absolute;
    left: 260px;
    width: 680px;
    height: 389px;
    border-radius: 18px;
    overflow: hidden;
    background: var(--card-black);
    box-shadow: 0 10px 30px rgba(0,0,0,0.45);
  }
  .card--back { top: 40px; }
  .card--front { top: 451px; }

  /* Back side */
  .back-photo {
    position: absolute;
    left: 0; top: 0;
    width: 562px; height: 100%;
    background:
      radial-gradient(ellipse 160px 120px at 78% 32%, rgba(220,154,85,0.95), rgba(220,154,85,0) 100%),
      radial-gradient(ellipse 150px 110px at 44% 72%, rgba(236,228,218,0.85), rgba(236,228,218,0) 100%),
      radial-gradient(ellipse 180px 140px at 60% 45%, rgba(46,32,22,0.55), rgba(46,32,22,0) 100%),
      radial-gradient(ellipse 140px 100px at 18% 78%, rgba(196,111,46,0.9), rgba(196,111,46,0) 100%),
      radial-gradient(ellipse 200px 80px at 40% 100%, rgba(78,47,30,0.95), rgba(78,47,30,0) 100%),
      radial-gradient(ellipse 160px 120px at 90% 80%, rgba(236,228,218,0.9), rgba(236,228,218,0) 100%),
      linear-gradient(125deg, var(--fur-cream) 0%, var(--fur-orange) 28%, var(--fur-amber) 50%, var(--fur-orange) 70%, var(--bark-brown) 100%);
  }
  .back-band {
    position: absolute;
    right: 0; top: 0;
    width: 118px; height: 100%;
    background: var(--band-black);
    display: flex;
    align-items: center;
    justify-content: center;
  }
  .back-band__text {
    transform: rotate(90deg);
    white-space: nowrap;
    text-align: center;
    color: var(--text-white);
  }
  .brand-name {
    font-weight: 700;
    letter-spacing: 0.01em;
    line-height: 1;
  }
  .brand-tagline {
    font-weight: 700;
    line-height: 1.1;
  }
  .back-band .brand-name { font-size: 30px; }
  .back-band .brand-tagline { font-size: 17px; margin-top: 6px; }

  /* Front side */
  .front-photo {
    position: absolute;
    right: 0; top: 0;
    width: 460px; height: 100%;
    background:
      radial-gradient(ellipse 130px 90px at 62% 34%, rgba(232,181,119,0.95), rgba(232,181,119,0) 100%),
      radial-gradient(ellipse 110px 70px at 60% 70%, rgba(217,169,160,0.9), rgba(217,169,160,0) 100%),
      radial-gradient(ellipse 90px 60px at 50% 78%, rgba(236,228,218,0.8), rgba(236,228,218,0) 100%),
      radial-gradient(ellipse 160px 200px at 92% 40%, rgba(46,32,22,0.6), rgba(46,32,22,0) 100%),
      radial-gradient(ellipse 120px 140px at 20% 70%, rgba(125,138,76,0.95), rgba(125,138,76,0) 100%),
      linear-gradient(110deg, var(--leaf-deep) 0%, var(--leaf-green) 24%, var(--fur-amber) 48%, var(--fur-orange) 70%, var(--fur-dark) 100%);
  }
  .front-fade {
    position: absolute;
    left: 0; top: 0;
    width: 100%; height: 100%;
    background: linear-gradient(90deg, var(--card-black) 0%, var(--card-black) 34%, rgba(11,11,11,0.7) 44%, rgba(11,11,11,0) 60%);
  }
  .front-info {
    position: absolute;
    left: 36px; top: 80px;
    color: var(--text-white);
  }
  .front-info .brand-name { font-size: 30px; }
  .front-info .brand-tagline { font-size: 16px; margin-top: 3px; }
  .contact { margin-top: 38px; }
  .contact__name {
    font-size: 18px;
    font-weight: 700;
    letter-spacing: 0.02em;
  }
  .contact__phones {
    margin-top: 16px;
    font-size: 16px;
    line-height: 1.4;
    padding-left: 24px;
  }
  .contact__phones b { font-weight: 700; }
  .contact__address {
    position: absolute;
    left: 36px; bottom: 30px;
    font-size: 12px;
    color: var(--text-soft);
  }
</style>
</head>
<body>
  <section class="card card--back" aria-label="Card back">
    <div class="back-photo" role="img" aria-label="Photo of a tiger resting its head beside an outstretched paw with sharp claws"></div>
    <div class="back-band">
      <div class="back-band__text">
        <div class="brand-name">BLUEBIRD MEADOW</div>
        <div class="brand-tagline">Shear Sharpening and Sales</div>
      </div>
    </div>
  </section>

  <section class="card card--front" aria-label="Card front">
    <div class="front-photo" role="img" aria-label="Photo of a snarling tiger showing its sharp teeth"></div>
    <div class="front-fade"></div>
    <div class="front-info">
      <div class="brand-name">BLUEBIRD MEADOW</div>
      <div class="brand-tagline">Shear Sharpening and Sales</div>
      <div class="contact">
        <div class="contact__name">MARCUS PELLINGHAM</div>
        <div class="contact__phones">
          <div><b>P:</b> (407)555-0174</div>
          <div><b>CP:</b> (321)555-0138</div>
        </div>
      </div>
    </div>
    <div class="contact__address">5127 Brennigan Lane Orlando FL 32899</div>
  </section>
</body>
</html>
```